Redesign Video/PIcture Check in Page

Redesign our current TetherWatchApp iPhone App checkin screens - Keep the design simple so that programmers do not have to do too much extra work to make your design work. - Look at the attached website screenshot for the overall look and feel, and color scheme - Convert the attached vector logo to iOS Icon format. - Deliver all graphics in the density required for iPhone XS Max. I will upload current check in pages that need to be reimagined. Check in needs to be more intutitive. Would like to add some gamification to the verification screen where they currently are required to enter series of random numbers. simple card game etc might work better. See TetherWatchapp in itunes and google play store. also visit quorvant-link.example or tetherwatchapp.example for more information about our company.
The Current Checkin Process:
A. Client receives alert to checkin or submits voluntary checkin
B. Clicks checkin button on home Screen.
Redesign from here:
C. Clicks on a check in from check in list screen(new screen)
D. Enters verification number(gamification something better than random numbers)
E. Opens Camera
D. Takes Selfie
F. submits photo
G. clicks check in
SEE CURRENT STEPS PIC I UPLOADED

Target Market(s)

Courts,Probation and parole,Attorneys,Sheriffs,Jails, Alternative sentencing

Colors
3277b5

Requirements
Must have
• Must be easy to navigate,Intuitive!
Nice to have
• Gamification of check in verification.
• Step by step process with next button or similar

```html
<!DOCTYPE html>
<html lang="en">
<head>
<meta charset="utf-8">
<title>Check-In Screens</title>
<link href="https://fonts.googleapis.com/css2?family=Lato:wght@400;700&display=swap" rel="stylesheet">
<style>
:root{
  --blob:#5b9bc4;
  --header:#5f9ec6;
  --navy:#1c2745;
  --button:#1f306e;
  --red:#e8174a;
  --ink:#1d1d1d;
  --muted:#9a9a9a;
  --faint:#cfd2da;
  --green:#1fc33d;
  --page:#ffffff;
}
*{box-sizing:border-box;margin:0;padding:0}
html,body{width:1200px;height:720px;overflow:hidden;background:var(--page);font-family:"Lato",sans-serif}
.canvas{position:relative;width:1200px;height:720px;overflow:hidden}
.blob{position:absolute;border-radius:50%;background:var(--blob)}
.blob-top-left{left:-160px;top:-168px;width:496px;height:496px}
.blob-top-mid{left:639px;top:38px;width:229px;height:229px}
.blob-bottom-mid{left:350px;top:518px;width:146px;height:146px}
.blob-bottom-right{left:828px;top:436px;width:410px;height:410px}
.screen{position:absolute;top:132px;width:210px;height:455px;background:#fff;overflow:hidden;box-shadow:0 12px 30px rgba(20,40,70,.12)}
.s1{left:46px}.s2{left:270px}.s3{left:494px}.s4{left:718px}.s5{left:942px}
.header{position:absolute;left:0;top:0;width:100%;height:102px;background:var(--header);color:#fff}
.status{position:absolute;top:11px;left:17px;right:14px;font-size:7px;font-weight:700;display:flex;justify-content:space-between;align-items:center}
.status svg{display:block}
.nav-icon{position:absolute;left:16px;top:42px}
.title{position:absolute;left:17px;top:69px;font-size:14px;font-weight:700}
.list{position:absolute;top:118px;left:18px;right:18px}
.item{position:relative;height:39.7px}
.item-name{font-size:8.5px;color:var(--ink)}
.item-date{font-size:7px;color:var(--muted);margin-top:3px}
.item svg{position:absolute;right:0;top:3px}
.tabbar{position:absolute;left:0;bottom:0;width:100%;height:70px;background:var(--navy);display:flex;padding:12px 8px 0}
.tab{flex:1;text-align:center;color:#fff;font-size:5px;font-weight:700;letter-spacing:.2px}
.tab svg{display:block;margin:0 auto 4px}
.tab.active{color:#3d7df0}
.indicator{position:absolute;bottom:9px;left:67px;width:77px;height:3px;border-radius:2px;background:#e3e3e3}
.tabbar .indicator{background:#0d1326;bottom:9px}
.meta{position:absolute;left:16px;top:124px}
.meta-date{font-size:7px;color:#8a8a8a}
.meta-title{font-size:10px;color:var(--ink);line-height:12.5px;margin-top:9px}
.camera{position:absolute;left:145px;top:119px;width:48px;height:48px;border:1px solid #dcdcdc;display:flex;align-items:center;justify-content:center}
.selfie{position:absolute;left:145px;top:119px;width:48px;height:48px;background:linear-gradient(135deg,#3b3631,#7a5a48 55%,#24283a)}
.dial{position:absolute;left:0;top:180px}
.hint{position:absolute;top:370px;width:100%;text-align:center;font-size:8px;color:#7d7d7d;line-height:11px}
.check-btn{position:absolute;left:51px;top:376px;width:108px;height:30px;background:var(--button);color:#fff;font-size:7.5px;display:flex;align-items:center;justify-content:center;gap:6px}
.dim{position:absolute;inset:0;background:rgba(20,22,28,.66)}
.s5 .header{z-index:0}
.dialog{position:absolute;left:26px;top:175px;width:159px;height:99px;background:#fff;border-radius:6px;text-align:center}
.dialog-title{font-size:10px;font-weight:700;color:var(--ink);margin-top:20px}
.dialog-text{font-size:8px;color:var(--ink);margin-top:4px}
.dialog-line{position:absolute;left:0;right:0;top:63px;border-top:1px solid #e4e4e4}
.dialog-ok{position:absolute;left:0;right:0;top:75px;font-size:9px;color:#2d7fe0}
.num{font-family:"Lato",sans-serif;font-size:9px;fill:#777;text-anchor:middle}
.num.light{fill:#c9c9c9}
.code{font-family:"Lato",sans-serif;font-size:14px;letter-spacing:4px;text-anchor:middle}
</style>
</head>
<body>
<div class="canvas">
  <div class="blob blob-top-left"></div>
  <div class="blob blob-top-mid"></div>
  <div class="blob blob-bottom-mid"></div>
  <div class="blob blob-bottom-right"></div>

  <!-- Screen 1: list -->
  <section class="screen s1">
    <div class="header">
      <div class="status"><span>9:41</span><svg width="36" height="6" viewBox="0 0 36 6"><rect x="0" y="4" width="2" height="2" fill="#fff"/><rect x="3" y="3" width="2" height="3" fill="#fff"/><rect x="6" y="1.5" width="2" height="4.5" fill="#fff"/><rect x="9" y="0" width="2" height="6" fill="#fff"/><path d="M14 2.5a5 5 0 0 1 7 0M15.5 4a2.8 2.8 0 0 1 4 0" stroke="#fff" fill="none" stroke-width="1"/><rect x="25" y="1" width="10" height="4.5" rx="1" fill="#fff"/></svg></div>
      <svg class="nav-icon" width="13" height="10" viewBox="0 0 13 10"><path d="M0 1h12M0 5h9M0 9h12" stroke="#fff" stroke-width="1.5"/></svg>
      <div class="title">Check - Ins</div>
    </div>
    <div class="list">
      <div class="item"><div class="item-name">Voluntary Check In Request</div><div class="item-date">Oct 20, 10:47pm</div><svg width="9" height="9" viewBox="0 0 9 9"><circle cx="4.5" cy="4.5" r="4.5" fill="#c7c7c7"/><path d="M2.4 4.6l1.4 1.4 2.8-2.8" stroke="#fff" fill="none" stroke-width="1"/></svg></div>
      <div class="item"><div class="item-name">Voluntary Check In Request</div><div class="item-date">Oct 20, 10:47pm</div><svg width="9" height="9" viewBox="0 0 9 9"><circle cx="4.5" cy="4.5" r="4.5" fill="#1fc33d"/><path d="M2.4 4.6l1.4 1.4 2.8-2.8" stroke="#fff" fill="none" stroke-width="1"/></svg></div>
      <div class="item"><div class="item-name">Soberiety Check In Request</div><div class="item-date">Oct 20, 10:47pm</div><svg width="9" height="9" viewBox="0 0 9 9"><circle cx="4.5" cy="4.5" r="4.5" fill="#1fc33d"/><path d="M2.4 4.6l1.4 1.4 2.8-2.8" stroke="#fff" fill="none" stroke-width="1"/></svg></div>
      <div class="item"><div class="item-name">Soberiety Check In Request</div><div class="item-date">Oct 20, 10:47pm</div><svg width="9" height="9" viewBox="0 0 9 9"><circle cx="4.5" cy="4.5" r="4.5" fill="#1fc33d"/><path d="M2.4 4.6l1.4 1.4 2.8-2.8" stroke="#fff" fill="none" stroke-width="1"/></svg></div>
      <div class="item"><div class="item-name">Voluntary Check In Request</div><div class="item-date">Oct 20, 10:47pm</div><svg width="9" height="9" viewBox="0 0 9 9"><circle cx="4.5" cy="4.5" r="4.5" fill="#c7c7c7"/><path d="M2.4 4.6l1.4 1.4 2.8-2.8" stroke="#fff" fill="none" stroke-width="1"/></svg></div>
      <div class="item"><div class="item-name">Soberiety Check In Request</div><div class="item-date">Oct 20, 10:47pm</div><svg width="9" height="9" viewBox="0 0 9 9"><circle cx="4.5" cy="4.5" r="4.5" fill="#1fc33d"/><path d="M2.4 4.6l1.4 1.4 2.8-2.8" stroke="#fff" fill="none" stroke-width="1"/></svg></div>
    </div>
    <nav class="tabbar">
      <div class="tab"><svg width="14" height="14" viewBox="0 0 14 14"><path d="M2 6.5L7 2l5 4.5V12H2z" stroke="#fff" fill="none" stroke-width="1"/><path d="M5.5 12V9h3v3" stroke="#fff" fill="none"/></svg>HOME</div>
      <div class="tab active"><svg width="14" height="16" viewBox="0 0 14 16"><path d="M7 14s-4.5-4.5-4.5-7.5a4.5 4.5 0 0 1 9 0C11.5 9.5 7 14 7 14z" stroke="#3d7df0" fill="none"/><circle cx="7" cy="6.5" r="1.6" stroke="#3d7df0" fill="none"/><circle cx="11" cy="2.5" r="2.3" fill="#e8174a"/></svg>CHECK INS</div>
      <div class="tab"><svg width="14" height="14" viewBox="0 0 14 14"><circle cx="7" cy="7" r="5.5" stroke="#fff" fill="none"/><path d="M1.5 7h11M7 1.5c-2.5 3-2.5 8 0 11M7 1.5c2.5 3 2.5 8 0 11" stroke="#fff" fill="none" stroke-width=".8"/></svg>MAPS</div>
      <div class="tab"><svg width="14" height="14" viewBox="0 0 14 14"><circle cx="7" cy="7" r="5.5" stroke="#fff" fill="none"/><circle cx="7" cy="4.3" r=".9" fill="#fff"/><path d="M7 6.2v4.5" stroke="#fff" stroke-width="1.2"/></svg>HOW TO</div>
      <div class="indicator"></div>
    </nav>
  </section>

  <!-- Screen 2: dial idle -->
  <section class="screen s2">
    <div class="header">
      <div class="status"><span>9:41</span><svg width="36" height="6" viewBox="0 0 36 6"><rect x="0" y="4" width="2" height="2" fill="#fff"/><rect x="3" y="3" width="2" height="3" fill="#fff"/><rect x="6" y="1.5" width="2" height="4.5" fill="#fff"/><rect x="9" y="0" width="2" height="6" fill="#fff"/><path d="M14 2.5a5 5 0 0 1 7 0M15.5 4a2.8 2.8 0 0 1 4 0" stroke="#fff" fill="none" stroke-width="1"/><rect x="25" y="1" width="10" height="4.5" rx="1" fill="#fff"/></svg></div>
      <svg class="nav-icon" width="13" height="10" viewBox="0 0 13 10"><path d="M12 5H1M5 1L1 5l4 4" stroke="#fff" fill="none" stroke-width="1.2"/></svg>
      <div class="title">Check - In</div>
    </div>
    <div class="meta"><div class="meta-date">Oct 20, 10:47pm</div><div class="meta-title">Voluntary Check<br>In Request</div></div>
    <div class="camera"><svg width="12" height="10" viewBox="0 0 12 10"><path d="M1 2.5h2.5l1-1.5h3l1 1.5H11V9H1z" fill="#bdbdbd"/><circle cx="6" cy="5.5" r="1.8" fill="#fff"/></svg></div>
    <svg class="dial" width="210" height="200" viewBox="0 0 210 200">
      <g class="nums">
        <text class="num" x="105" y="42">0</text>
        <text class="num" x="105" y="42" transform="rotate(36 105 100)">1</text>
        <text class="num" x="105" y="42" transform="rotate(72 105 100)">2</text>
        <text class="num" x="105" y="42" transform="rotate(108 105 100)">3</text>
        <text class="num" x="105" y="42" transform="rotate(144 105 100)">4</text>
        <text class="num" x="105" y="42" transform="rotate(180 105 100)">5</text>
        <text class="num" x="105" y="42" transform="rotate(216 105 100)">6</text>
        <text class="num" x="105" y="42" transform="rotate(252 105 100)">7</text>
        <text class="num" x="105" y="42" transform="rotate(288 105 100)">8</text>
        <text class="num" x="105" y="42" transform="rotate(324 105 100)">9</text>
      </g>
      <circle cx="105" cy="100" r="44" fill="none" stroke="var(--red)" stroke-width="2.4"/>
      <path d="M101.5 58l3.5-8 3.5 8z" fill="var(--red)"/>
      <text class="code" x="107" y="105" fill="#cfcfcf">6295</text>
    </svg>
    <div class="hint">Operate the dial to<br>enter the code above</div>
    <div class="indicator"></div>
  </section>

  <!-- Screen 3: dial in progress -->
  <section class="screen s3">
    <div class="header">
      <div class="status"><span>9:41</span><svg width="36" height="6" viewBox="0 0 36 6"><rect x="0" y="4" width="2" height="2" fill="#fff"/><rect x="3" y="3" width="2" height="3" fill="#fff"/><rect x="6" y="1.5" width="2" height="4.5" fill="#fff"/><rect x="9" y="0" width="2" height="6" fill="#fff"/><path d="M14 2.5a5 5 0 0 1 7 0M15.5 4a2.8 2.8 0 0 1 4 0" stroke="#fff" fill="none" stroke-width="1"/><rect x="25" y="1" width="10" height="4.5" rx="1" fill="#fff"/></svg></div>
      <svg class="nav-icon" width="13" height="10" viewBox="0 0 13 10"><path d="M12 5H1M5 1L1 5l4 4" stroke="#fff" fill="none" stroke-width="1.2"/></svg>
      <div class="title">Check - In</div>
    </div>
    <div class="meta"><div class="meta-date">Oct 20, 10:47pm</div><div class="meta-title">Voluntary Check<br>In Request</div></div>
    <div class="camera"><svg width="12" height="10" viewBox="0 0 12 10"><path d="M1 2.5h2.5l1-1.5h3l1 1.5H11V9H1z" fill="#bdbdbd"/><circle cx="6" cy="5.5" r="1.8" fill="#fff"/></svg></div>
    <svg class="dial" width="210" height="200" viewBox="0 0 210 200">
      <g class="nums">
        <text class="num" x="105" y="42">0</text>
        <text class="num" x="105" y="42" transform="rotate(36 105 100)">1</text>
        <text class="num" x="105" y="42" transform="rotate(72 105 100)">2</text>
        <text class="num" x="105" y="42" transform="rotate(108 105 100)">3</text>
        <text class="num" x="105" y="42" transform="rotate(144 105 100)">4</text>
        <text class="num" x="105" y="42" transform="rotate(180 105 100)">5</text>
        <text class="num" x="105" y="42" transform="rotate(216 105 100)">6</text>
        <text class="num" x="105" y="42" transform="rotate(252 105 100)">7</text>
        <text class="num" x="105" y="42" transform="rotate(288 105 100)">8</text>
        <text class="num" x="105" y="42" transform="rotate(324 105 100)">9</text>
      </g>
      <circle cx="105" cy="100" r="44" fill="none" stroke="var(--navy)" stroke-width="2.4"/>
      <path d="M101.5 58l3.5-8 3.5 8z" fill="var(--navy)" transform="rotate(-36 105 100)"/>
      <text class="code" x="107" y="105"><tspan fill="var(--navy)" font-weight="700">629</tspan><tspan fill="#cfcfcf">5</tspan></text>
    </svg>
    <div class="hint">Operate the dial to<br>enter the code above</div>
    <div class="indicator"></div>
  </section>

  <!-- Screen 4: verified with photo -->
  <section class="screen s4">
    <div class="header">
      <div class="status"><span>9:41</span><svg width="36" height="6" viewBox="0 0 36 6"><rect x="0" y="4" width="2" height="2" fill="#fff"/><rect x="3" y="3" width="2" height="3" fill="#fff"/><rect x="6" y="1.5" width="2" height="4.5" fill="#fff"/><rect x="9" y="0" width="2" height="6" fill="#fff"/><path d="M14 2.5a5 5 0 0 1 7 0M15.5 4a2.8 2.8 0 0 1 4 0" stroke="#fff" fill="none" stroke-width="1"/><rect x="25" y="1" width="10" height="4.5" rx="1" fill="#fff"/></svg></div>
      <svg class="nav-icon" width="13" height="10" viewBox="0 0 13 10"><path d="M12 5H1M5 1L1 5l4 4" stroke="#fff" fill="none" stroke-width="1.2"/></svg>
      <div class="title">Check - In</div>
    </div>
    <div class="meta"><div class="meta-date">Oct 20, 10:47pm</div><div class="meta-title">Voluntary Check<br>In Request</div></div>
    <div class="selfie" role="img" aria-label="Selfie photo taken for the check-in"></div>
    <svg class="dial" width="210" height="200" viewBox="0 0 210 200">
      <g class="nums">
        <text class="num light" x="105" y="42">0</text>
        <text class="num light" x="105" y="42" transform="rotate(36 105 100)">1</text>
        <text class="num light" x="105" y="42" transform="rotate(72 105 100)">2</text>
        <text class="num light" x="105" y="42" transform="rotate(108 105 100)">3</text>
        <text class="num light" x="105" y="42" transform="rotate(144 105 100)">4</text>
        <text class="num light" x="105" y="42" transform="rotate(180 105 100)">5</text>
        <text class="num light" x="105" y="42" transform="rotate(216 105 100)">6</text>
        <text class="num light" x="105" y="42" transform="rotate(252 105 100)">7</text>
        <text class="num light" x="105" y="42" transform="rotate(288 105 100)">8</text>
        <text class="num light" x="105" y="42" transform="rotate(324 105 100)">9</text>
      </g>
      <circle cx="105" cy="100" r="44" fill="none" stroke="var(--faint)" stroke-width="2"/>
      <path d="M98 100l5 5 9-10" stroke="var(--navy)" fill="none" stroke-width="1.8"/>
    </svg>
    <div class="check-btn"><svg width="7" height="9" viewBox="0 0 7 9"><path d="M3.5 9S0 5.5 0 3.5a3.5 3.5 0 0 1 7 0C7 5.5 3.5 9 3.5 9z" fill="#fff"/><circle cx="3.5" cy="3.5" r="1.2" fill="var(--button)"/></svg>Check - In</div>
    <div class="indicator"></div>
  </section>

  <!-- Screen 5: success dialog -->
  <section class="screen s5">
    <div class="header">
      <div class="status"><span>9:41</span><svg width="36" height="6" viewBox="0 0 36 6"><rect x="0" y="4" width="2" height="2" fill="#fff"/><rect x="3" y="3" width="2" height="3" fill="#fff"/><rect x="6" y="1.5" width="2" height="4.5" fill="#fff"/><rect x="9" y="0" width="2" height="6" fill="#fff"/><path d="M14 2.5a5 5 0 0 1 7 0M15.5 4a2.8 2.8 0 0 1 4 0" stroke="#fff" fill="none" stroke-width="1"/><rect x="25" y="1" width="10" height="4.5" rx="1" fill="#fff"/></svg></div>
      <svg class="nav-icon" width="13" height="10" viewBox="0 0 13 10"><path d="M12 5H1M5 1L1 5l4 4" stroke="#fff" fill="none" stroke-width="1.2"/></svg>
      <div class="title">Check - In</div>
    </div>
    <div class="meta"><div class="meta-date">Oct 20, 10:47pm</div><div class="meta-title">Voluntary Check<br>In Request</div></div>
    <div class="selfie" role="img" aria-label="Selfie photo taken for the check-in"></div>
    <svg class="dial" width="210" height="200" viewBox="0 0 210 200">
      <g class="nums">
        <text class="num light" x="105" y="42" transform="rotate(108 105 100)">3</text>
        <text class="num light" x="105" y="42" transform="rotate(144 105 100)">4</text>
        <text class="num light" x="105" y="42" transform="rotate(180 105 100)">5</text>
        <text class="num light" x="105" y="42" transform="rotate(216 105 100)">6</text>
        <text class="num light" x="105" y="42" transform="rotate(252 105 100)">7</text>
      </g>
      <circle cx="105" cy="100" r="44" fill="none" stroke="var(--faint)" stroke-width="2"/>
      <path d="M98 100l5 5 9-10" stroke="var(--navy)" fill="none" stroke-width="1.8"/>
    </svg>
    <div class="check-btn"><svg width="7" height="9" viewBox="0 0 7 9"><path d="M3.5 9S0 5.5 0 3.5a3.5 3.5 0 0 1 7 0C7 5.5 3.5 9 3.5 9z" fill="#fff"/><circle cx="3.5" cy="3.5" r="1.2" fill="var(--button)"/></svg>Check - In</div>
    <div class="indicator"></div>
    <div class="dim"></div>
    <div class="dialog">
      <div class="dialog-title">Success</div>
      <div class="dialog-text">Check in Completed</div>
      <div class="dialog-line"></div>
      <div class="dialog-ok">OK</div>
    </div>
  </section>
</div>
</body>
</html>
```